Give Bright Oak an Online Presence!

Bright Oak Property Maintenance is an Australian Owned property maintenance company who needs a stand out online presence.

BOK maintains many buildings and sites and wants to appeal to a corporate professional market with their brand new website. BOK is essentially a handyman service offering all maintenance services to home owners, office managers, real estate agents and strata managers.

The Website:
We need a corporate website that appeals to our broader customer base (property owners, property managers, office managers) the copy is being written by a professional so use filler text for now.

Things that we want:
Home page that sets us apart and appeals to the corporate and residential market. The home page needs to not focus on either the residential or commercial market. The home page should focus on our logo and branding. We have a logo already and it is attached to the brief, please use it and try to consider the colour pallette that goes with it. Whilst we want the site to appear strong and manly it is important to remember that 95% of our customers are female so we need the site to be appealing to women. Women need to believe that we are strong, dependable and trustworthy.
We'd like a quote page and potentially also the ability to get a quote from the home page (please don't put it in if it ruins the overall feel of the home page)
An "about us" page
A contact us page
A blog that's built in (we don't want to link to an external blog)
(overall we'd expect to have 6 or 7 pages total)

The site will also need coding - we expect this to be done in a separate project but need you to consider a few things about the coding side of things.

It needs to be iPhone and iPad compatible.

We'd like you to suggest the best CMS that you would use or if you would suggest not using a CMS please let us know with your submissions.

Target Market(s)

Property owners, office managers and property managers who need maintenance on buildings (So all of them)

Industry/Entity Type

Property Maintenance

Requirements
Must have
• Our Logo
Home page
About Us
Residential
Commercial
Real Estate/Strata
Contact Us/Quote
Blog
Nice to have
• Quote form included in home page
Movement on the home page at least
Should not have
• other logos, too much colour
NO FLASH

```html
<!DOCTYPE html>
<html lang="en">
<head>
<meta charset="utf-8">
<title>Bright Oak Property Maintenance</title>
<link rel="stylesheet" href="https://fonts.googleapis.com/css2?family=Arimo:wght@400;700&family=PT+Sans:wght@400;700&display=swap">
<style>
:root{
  --orange:#f7941d;
  --orange-light:#fbb25a;
  --maroon:#5a0e0e;
  --maroon-dark:#3c0808;
  --blue:#4a6cb0;
  --black:#000;
  --ink:#111;
  --white:#fff;
  --field:#dcdcdc;
  --grey:#666;
}
*{box-sizing:border-box;margin:0;padding:0}
html,body{width:960px;height:1200px;overflow:hidden;background:var(--white)}
body{font-family:"Arimo",Arial,sans-serif;color:var(--ink)}
.page{position:relative;width:960px;height:1200px;overflow:hidden}
.abs{position:absolute}
.edge-top{left:0;top:0;width:960px;height:6px;background:var(--black)}
.edge-bottom{left:0;top:1194px;width:960px;height:6px;background:var(--black)}

.follow{left:738px;top:11px;font-size:10px;color:var(--orange);display:flex;align-items:center;gap:5px}
.follow .social{width:14px;height:14px;border-radius:3px;background:#3f6fa8}
.follow .social.alt{background:#5bb6e0}
.newsletter{left:652px;top:33px;font-size:9px;color:#333}
.newsletter-field{left:710px;top:30px;width:157px;height:19px;border:1px solid #bbb;font-size:8px;padding:4px 5px;color:#333}
.btn-small{background:var(--maroon);color:var(--white);font-size:8px;text-align:center;border-radius:2px}
.newsletter-submit{left:824px;top:54px;width:42px;height:13px;line-height:13px}

.bands{left:0;top:0}
.logo-card{left:382px;top:46px;width:196px;height:124px;background:var(--white);border:1px solid #bbb;box-shadow:0 3px 6px rgba(0,0,0,.35);transform:rotate(1deg);display:flex;flex-direction:column;align-items:center;justify-content:center;gap:6px}
.logo-mark{width:18px;height:18px;background:var(--orange)}
.logo-name{font-weight:700;font-size:13px;color:var(--orange);text-align:center;line-height:1.2;width:150px}

.nav a{position:absolute;font-size:14px;color:var(--maroon-dark);text-decoration:none;top:100px}
.nav .current{left:116px;top:95px;width:66px;height:27px;line-height:27px;text-align:center;background:var(--maroon);color:var(--white);border:1px solid #2a0505}
.blog-board{left:790px;top:138px;width:72px;height:54px;background:#1a1a1a;border:3px solid #a0784a;color:var(--white);font-size:17px;font-weight:700;display:flex;align-items:center;justify-content:center}

.hero-art{left:456px;top:120px;width:440px;height:344px;background:linear-gradient(90deg,rgba(255,255,255,0) 0%,#dfe6f2 22%,#b9a486 60%,#e07a2c 85%,rgba(255,255,255,0) 100%);clip-path:polygon(10% 25%,60% 8%,85% 0,100% 40%,100% 100%,12% 100%,5% 60%)}

.headline{left:111px;top:210px;color:var(--ink)}
.headline .l1{font-size:17px;position:absolute;left:2px;top:14px;white-space:nowrap}
.headline .done{font-size:35px;color:var(--orange);position:absolute;left:147px;top:0}
.headline .l2{font-size:13px;position:absolute;left:36px;top:40px;white-space:nowrap}
.headline .amp{font-size:24px;position:absolute;left:270px;top:28px}
.headline .l3{font-size:17px;position:absolute;left:0;top:70px;white-space:nowrap}
.headline .big{font-size:40px;color:var(--maroon);position:absolute;left:168px;top:50px}
.headline .or{font-size:17px;position:absolute;left:233px;top:70px}
.headline .small{font-size:40px;color:var(--blue);position:absolute;left:258px;top:50px}
.intro{left:112px;top:307px;width:348px;font-size:11px;line-height:14px;text-align:center;letter-spacing:-.2px}

.quote-btn{left:228px;top:391px;width:161px;height:35px;border-radius:8px;background:linear-gradient(var(--orange-light),var(--orange));color:var(--white);font-size:19px;line-height:35px;padding-left:10px}
.free-badge{left:178px;top:384px;width:48px;height:48px;border-radius:50%;background:#c0161a;color:var(--white);font-size:11px;font-weight:700;line-height:48px;text-align:center;transform:rotate(-18deg);box-shadow:0 0 0 3px #d92a2a}

.services-tab{left:661px;top:465px;width:171px;height:37px;font-size:22px;line-height:37px;padding-left:14px;color:var(--white)}
.services-tab span{color:var(--orange)}
.card{position:absolute;top:520px;width:219px;height:199px;background:var(--white);border:2px solid var(--maroon-dark);overflow:hidden}
.card h3{font-weight:400;font-size:24px;color:var(--maroon-dark);text-align:center;margin-top:8px}
.card .photo{margin:5px auto 0;width:196px;height:83px;border:1px solid #999}
.card p{font-size:7.5px;line-height:10.5px;text-align:center;color:#333;margin:14px 8px 0}
.card .more{position:absolute;right:0;bottom:0;width:64px;height:20px;background:var(--maroon);color:var(--white);font-size:7.5px;line-height:20px;text-align:right;padding-right:8px;clip-path:polygon(14% 0,100% 0,100% 100%,0 100%)}
.photo.pipes{background:linear-gradient(120deg,#e8e3dd,#c08060 45%,#79a9cf 70%,#d8d2cb)}
.photo.wires{background:linear-gradient(160deg,#2d2a28,#b97448 45%,#c7d36a 65%,#4c7fc0 85%,#2d2a28)}
.photo.wood{background:linear-gradient(120deg,#efe7df,#d9b79f 40%,#8a8a8a 60%,#e9dccf)}

.dots{left:414px;top:730px;width:158px;height:25px;display:flex;gap:7px;justify-content:center;align-items:center;padding-top:2px}
.dots i{width:9px;height:9px;border-radius:50%;background:var(--white)}
.dots i.on{background:var(--maroon)}

.about{left:108px;top:782px;width:442px;color:var(--white)}
.about h2{font-weight:400;font-size:24px;white-space:nowrap}
.about h2 small{font-size:11px}
.about h2 span{color:var(--orange)}
.about p{font-size:10px;line-height:14px;letter-spacing:-.15px;margin-top:-2px}
.divider{left:558px;top:796px;width:1px;height:148px;background:#555}
.finder{left:570px;top:788px;width:284px}
.finder h2{font-weight:400;font-size:16px;color:var(--white);white-space:nowrap}
.finder h2 span{color:var(--orange)}
.select{position:absolute;left:0;width:284px;height:27px;background:var(--field);font-size:10px;line-height:27px;padding-left:9px;color:#333}
.select::after{content:"";position:absolute;right:0;top:0;width:28px;height:27px;background:var(--maroon)}
.select b{position:absolute;right:9px;top:11px;width:0;height:0;border-left:5px solid transparent;border-right:5px solid transparent;border-top:5px solid var(--white);z-index:1}
.finder-submit{left:792px;top:926px;width:62px;height:21px;line-height:21px;font-size:10px;clip-path:polygon(12% 0,100% 0,100% 100%,0 100%)}

.testimonial-line{left:250px;width:460px;height:1px;background:linear-gradient(90deg,transparent,#ccc,transparent);box-shadow:0 2px 4px rgba(0,0,0,.1)}
.testimonial-title{left:0;width:920px;top:1013px;text-align:center;font-size:19px}
.testimonial-title span{color:var(--orange)}
.testimonial-text{left:228px;top:1042px;width:524px;text-align:center;font-size:10px;line-height:13.5px;color:#222}
.arrow{top:1048px;width:10px;height:10px;border-left:1.5px solid #333;border-bottom:1.5px solid #333}
.arrow.prev{left:188px;transform:rotate(45deg)}
.arrow.next{left:784px;transform:rotate(-135deg)}

.footer-links{left:113px;top:1140px;font-size:10px;color:var(--ink);white-space:nowrap}
.footer-links span{margin:0 4px;color:var(--maroon)}
.copyright{left:113px;top:1177px;font-family:"PT Sans",Arial,sans-serif;font-size:9px;color:var(--maroon-dark)}
.footer-logo{left:764px;top:1150px;width:100px;display:flex;flex-direction:column;align-items:center;gap:4px}
.footer-logo .logo-mark{width:14px;height:14px;background:var(--maroon-dark)}
.footer-logo .logo-name{font-size:9px;color:var(--maroon-dark);width:100px}
</style>
</head>
<body>
<div class="page">
  <div class="abs edge-top"></div>

  <div class="abs follow">Follow Us On :<i class="social"></i><i class="social"></i><i class="social alt"></i></div>
  <div class="abs newsletter">Newsletter :</div>
  <div class="abs newsletter-field">E-mail</div>
  <div class="abs btn-small newsletter-submit">Submit</div>

  <svg class="abs bands" width="960" height="1200" viewBox="0 0 960 1200">
    <polygon points="90,70 392,70 392,144 90,152" fill="var(--orange)"/>
    <polygon points="572,78 869,78 869,136 572,140" fill="var(--orange)"/>
    <rect x="90" y="740" width="779" height="246" fill="var(--black)"/>
    <polygon points="118,462 844,462 869,768 572,760 572,744 414,744 90,744" fill="var(--orange)"/>
    <polygon points="661,465 832,465 832,502 672,502" fill="var(--maroon-dark)"/>
    <rect x="414" y="730" width="158" height="26" fill="var(--black)"/>
    <polygon points="90,1110 869,1150 869,1194 90,1194" fill="var(--orange)"/>
  </svg>

  <div class="abs hero-art" role="img" aria-label="Line drawing of a house cross-section behind a smiling worker in a yellow hard hat, hi-vis vest and ear muffs"></div>

  <div class="abs logo-card">
    <div class="logo-mark"></div>
    <div class="logo-name">Bright Oak Property Maintenance</div>
  </div>

  <nav class="nav">
    <a class="abs current" href="#">HOME</a>
    <a href="#" style="left:200px">About Us</a>
    <a href="#" style="left:290px">Residential</a>
    <a href="#" style="left:586px">Commercial</a>
    <a href="#" style="left:691px">Real Estate</a>
    <a href="#" style="left:790px">Contact Us</a>
  </nav>
  <div class="abs blog-board">Blog</div>

  <div class="abs headline">
    <span class="l1">We Can Make It</span>
    <span class="done">Done</span>
    <span class="l2">Whenever, Wherever, Whatever</span>
    <span class="amp">&amp;</span>
    <span class="l3">However the job is</span>
    <span class="big">Big</span>
    <span class="or">or</span>
    <span class="small">Small</span>
  </div>
  <p class="abs intro">Specialising in plastering, ames taping, plumbing and bathrooms; free quotations are available on any project whether large or small. Each job is quoted on an individual basis, giving you a tailored, cost effective quote for your specific project.</p>

  <div class="abs quote-btn">Make A Quote</div>
  <div class="abs free-badge">FREE!</div>

  <div class="abs services-tab">Our <span>Services</span></div>

  <article class="card" style="left:138px">
    <h3>Plumbing</h3>
    <div class="photo pipes" role="img" aria-label="Copper pipe fittings and blue plumbing pipes"></div>
    <p>At vero eos et accusamus et iusto odio dignissimos ducimus qui blanditiis praesentium voluptatum deleniti atque corrupti quos dolores et quas</p>
    <div class="more">Read More</div>
  </article>
  <article class="card" style="left:367px">
    <h3>Electrical</h3>
    <div class="photo wires" role="img" aria-label="Close-up of stripped copper electrical cables"></div>
    <p>At vero eos et accusamus et iusto odio dignissimos ducimus qui blanditiis praesentium voluptatum deleniti atque corrupti quos dolores et quas</p>
    <div class="more">Read More</div>
  </article>
  <article class="card" style="left:600px">
    <h3>Carpentry</h3>
    <div class="photo wood" role="img" aria-label="Hands working with a hand plane and tools on timber"></div>
    <p>At vero eos et accusamus et iusto odio dignissimos ducimus qui blanditiis praesentium voluptatum deleniti atque corrupti quos dolores et quas</p>
    <div class="more">Read More</div>
  </article>

  <div class="abs dots"><i class="on"></i><i></i><i></i><i></i><i></i><i></i><i></i><i></i></div>

  <section class="abs about">
    <h2>Hello! <small>We Are</small> Bright <span>Oak...</span></h2>
    <p>At vero eos et accusamus et iusto odio dignissimos ducimus qui blanditiis praesentium voluptatum deleniti atque corrupti quos dolores et quas molestias excepturi sint occaecati cupiditate non provident, similique sunt in culpa qui officia deserunt mollitia animi, id est laborum et dolorum fuga. Et harum quidem rerum facilis est et expedita distinctio. Nam libero tempore, cum soluta nobis est eligendi optio cumque nihil impedit quo minus id quod maxime placeat facere possimus, omnis voluptas assumenda est, omnis dolor repellendus. Temporibus autem quibusdam et aut officiis debitis aut rerum necessitatibus saepe eveniet ut et voluptates repudiandae sint et molestiae non recusandae. Itaque earum rerum hic tenetur a sapiente delectus, ut aut reiciendis voluptatibus maiores alias consequatur aut perferendis doloribus asperiores repellat.</p>
  </section>
  <div class="abs divider"></div>

  <section class="abs finder">
    <h2>Find Your Local <span>MaintenanceMan</span></h2>
    <div class="select" style="top:37px">Please Select Your State<b></b></div>
    <div class="select" style="top:69px">Please Select Your City<b></b></div>
    <div class="select" style="top:102px">Please Select Your Region<b></b></div>
  </section>
  <div class="abs btn-small finder-submit">Submit</div>

  <div class="abs testimonial-line" style="top:1004px"></div>
  <h2 class="abs testimonial-title" style="font-weight:400;left:20px">Client <span>Testimonial</span></h2>
  <p class="abs testimonial-text">“At vero eos et accusamus et iusto odio dignissimos ducimus qui blanditiis praesentium voluptatum deleniti atque corrupti quos dolores et quas molestias excepturi sint occaecati cupiditate non provident, similique sunt in culpa qui officia deserunt mollitia animAi, id est laborum et dolorum fuga.”</p>
  <div class="abs arrow prev"></div>
  <div class="abs arrow next"></div>
  <div class="abs testimonial-line" style="top:1100px"></div>

  <div class="abs footer-links">Home<span>|</span>About Us<span>|</span>Residential<span>|</span>Commercial<span>|</span>Real Estate<span>|</span>Contact Us<span>|</span>Blog</div>
  <div class="abs copyright">©2012 All Rights Reserved By Bright Oak Property Maintenance</div>
  <div class="abs footer-logo">
    <div class="logo-mark"></div>
    <div class="logo-name">Bright Oak Property Maintenance</div>
  </div>

  <div class="abs edge-bottom"></div>
</div>
</body>
</html>
```